Broschüren-Design für Versicherungsagenten
Zielgruppe
Ich bin mit KL-Vorsorge als unabhängiger Versicherungsagent Selbstständig. (www.kl-vorsorge.de)
Ich habe mich auf die Absicherung von biometrischen Risiken spezialisiert - die auch in der Broschüre Thematisiert werden sollen. Das Oberthema der Broschüre ist 'biometrische Risiken'. Dies soll dann auf die Themen: Arbeitskraft, Langlebigkeit und Pflege heruntergebrochen werden.
Zielgruppe sind vor allem junge Menschen, die gerade erst eine Ausbildung gestartet oder ihr Studium beendet haben.
Aufgabenstellung
Das Design sollte die drei Hauptbereiche: Arbeitskraft, Langlebigkeit und Pflege, leicht verständlich dem Kunden veranschaulichen. Texte, Informationen und Grafiken (in der Reihenfolge, so wie ich mir das vorstelle) sind als Datei beigefügt.
Das ganze soll im DIN A4 Format gedruckt werden, wobei ich auf einen Hochwertigen Druck inklusive Druckveredelung hohen Wert lege.

```html
<!DOCTYPE html>
<html lang="de">
<head>
<meta charset="utf-8">
<title>KL-Vorsorge – Broschüre Biometrische Risiken</title>
<link href="https://fonts.googleapis.com/css2?family=Open+Sans:wght@300;400;600;700&display=swap" rel="stylesheet">
<style>
:root{
  --teal:#1ea99b;
  --teal-light:#2db7aa;
  --teal-dark:#168d82;
  --grey:#c9c9c9;
  --grey-mid:#d6d6d6;
  --grey-light:#e6e6e6;
  --paper:#f5f5f5;
  --white:#ffffff;
  --ink:#2e2e2e;
  --ink-soft:#555555;
  --ink-light:#6f6f6f;
  --box-blue:#cfe4ea;
  --alert:#d23b3b;
  --stage:#e3e3e7;
}
*{margin:0;padding:0;box-sizing:border-box}
html,body{width:1200px;height:2527px;overflow:hidden;background:var(--stage)}
body{position:relative;font-family:"Open Sans",Arial,sans-serif;color:var(--ink)}
.spread{position:absolute;left:40px;width:1120px;height:792px;background:var(--paper);box-shadow:0 10px 30px rgba(0,0,0,.12);display:flex}
.spread--cover{top:38px}
.spread--work{top:868px}
.spread--care{top:1698px}
.page{position:relative;width:560px;height:792px;overflow:hidden}
.page + .page{box-shadow:inset 1px 0 0 rgba(0,0,0,.06)}
.page-bg{position:absolute;inset:0;width:560px;height:792px}
.block{position:absolute}
.small{font-size:9px;line-height:1.45;color:var(--ink-soft)}
.tiny{font-size:7.5px;line-height:1.35;color:var(--ink-soft)}
.white{color:var(--white)}
.brand{display:flex;align-items:center;gap:8px;font-weight:700;font-size:22px;color:var(--ink)}
.brand-dot{width:26px;height:26px;border-radius:50%;background:var(--ink)}
.brand--light{color:var(--white)}
.brand--light .brand-dot{background:var(--ink)}
.band-label{font-weight:600;font-size:14px;color:var(--white);letter-spacing:.3px}
.cover-title{font-weight:700;font-size:27px;line-height:1.25;color:var(--white)}
.cover-sub{font-size:9.5px;color:var(--white);margin-top:6px}
.topics{font-weight:700;font-size:12px;color:var(--ink)}
.contact{font-size:11px;line-height:2.1;color:rgba(255,255,255,.9)}
.section-head{left:40px;top:38px;width:480px;border-bottom:1px dashed var(--teal);padding-bottom:6px}
.section-head .kicker{font-weight:700;font-size:14px}
.section-head .question{font-weight:600;font-size:13px;color:var(--ink)}
.display{font-weight:300;font-size:27px;line-height:1.2;color:var(--ink-light)}
.teal-text{color:var(--teal);font-weight:600}
.placeholder{background:linear-gradient(180deg,#7d7f80,#5c5e5f);border-radius:3px}
.stat{position:absolute;width:70px;text-align:center}
.stat .icon{height:34px;width:24px;margin:0 auto 4px;background:#5f6163;border-radius:3px}
.stat .icon--teal{background:var(--teal)}
.stat .num{font-weight:700;font-size:10px}
.stat .lbl{font-size:7px;line-height:1.3;color:var(--ink-soft)}
.rotated{transform-origin:0 0;transform:rotate(20.56deg);white-space:nowrap}
.band-statement{font-weight:700;font-size:15px;color:var(--white)}
.solutions-title{font-weight:600;font-size:10px;color:var(--ink)}
.solution{position:absolute;width:66px;height:66px;border-radius:50%;background:var(--teal);display:flex;flex-direction:column;align-items:center;justify-content:center;color:var(--white);font-size:6.5px;text-align:center;line-height:1.2;padding:6px}
.solution svg{width:22px;height:22px;margin-bottom:3px}
.pension-table{width:300px;font-size:8.5px;color:var(--ink-soft);border-collapse:collapse}
.pension-table td{padding:1px 0}
.pension-table .head{font-weight:700;color:var(--ink)}
.pension-table .amount{font-weight:700;color:var(--ink);text-align:right}
.gap-label{font-weight:700;font-size:15px;line-height:1.2;color:var(--white)}
.calc-box{position:absolute;background:var(--box-blue);padding:10px 10px 8px 36px;width:225px}
.calc-box .calc-icon{position:absolute;left:9px;top:10px;width:18px;height:22px;border-radius:2px;background:#4a90b0}
.calc-box table{width:100%;font-size:7.5px;color:var(--ink-soft);border-collapse:collapse}
.calc-box td{padding:1px 0}
.calc-box td:last-child{text-align:right}
.calc-box .title{font-weight:700;color:var(--ink)}
.calc-box .due{color:var(--alert);font-weight:700}
.center-q{font-weight:700;font-size:11px}
</style>
</head>
<body>

<!-- Outside: cover and back -->
<section class="spread spread--cover">
  <div class="page page--cover">
    <svg class="page-bg" viewBox="0 0 560 792" aria-hidden="true">
      <rect width="560" height="792" fill="var(--paper)"/>
      <polygon points="0,0 560,0 560,92 0,150" fill="var(--grey)"/>
      <polygon points="40,146 560,92 560,120 40,174" fill="var(--teal)"/>
      <polygon points="0,250 560,470 0,650" fill="var(--teal)"/>
      <polygon points="0,650 560,470 560,792 0,792" fill="var(--grey-mid)"/>
      <polygon points="290,792 560,470 560,792" fill="var(--grey-light)"/>
    </svg>
    <div class="block brand" style="left:34px;top:36px"><span class="brand-dot"></span>KL-Vorsorge</div>
    <div class="block band-label" style="left:300px;top:114px">Biometrische Risiken</div>
    <div class="block" style="left:170px;top:190px;width:350px;text-align:right">
      <div class="topics">Arbeitskraft • Langlebigkeit • Pflege</div>
      <p class="small" style="margin-top:6px">Viele Menschen sind bisher nur unzureichend über das große Potenzial dieser Risiken und vor allem ihre existenzbedrohenden Folgen aufgeklärt.</p>
    </div>
    <div class="block" style="left:34px;top:380px;width:400px">
      <h1 class="cover-title">„Welche Versicherungen brauche ich denn wirklich?“</h1>
      <p class="cover-sub">Wir sind Ihr Spezialist auf dem Gebiet der biometrischen Risikoabsicherung.</p>
    </div>
    <p class="block small" style="left:260px;top:650px;width:260px;text-align:right">Auf den nachfolgenden Seiten finden Sie einige Erläuterungen zu den wichtigsten Aspekten in der Absicherung von biometrischen Risiken.</p>
  </div>

  <div class="page page--back">
    <svg class="page-bg" viewBox="0 0 560 792" aria-hidden="true">
      <rect width="560" height="792" fill="var(--grey-mid)"/>
      <polygon points="0,0 50,0 560,330 560,372" fill="var(--teal-light)"/>
      <polygon points="0,12 560,372 560,398 0,470" fill="var(--paper)"/>
      <polygon points="0,470 560,398 560,792 210,792" fill="var(--teal)"/>
    </svg>
    <p class="block small" style="left:30px;top:235px;width:270px">Du hast Fragen zu meiner Arbeit?<br>Oder Unklarheiten zu einer bestimmten Versicherung?<br>Melde dich bei mir!</p>
    <div class="block" style="left:270px;top:520px">
      <div class="brand brand--light"><span class="brand-dot"></span>KL-Vorsorge</div>
      <address class="contact" style="font-style:normal;margin-top:10px;padding-left:34px">
        Belwig Max<br>Lindenweg 8<br>89340 Leipheim<br>Telefon: 08221 5550184<br>Mobil: 0176 55501234<br>E-Mail: max.belwig@postfach-mail.de
      </address>
    </div>
  </div>
</section>

<!-- Inside: work capacity and longevity -->
<section class="spread spread--work">
  <div class="page page--work">
    <svg class="page-bg" viewBox="0 0 560 792" aria-hidden="true">
      <rect width="560" height="792" fill="var(--paper)"/>
      <polygon points="0,430 560,640 560,682 0,472" fill="var(--teal)"/>
      <polygon points="0,472 560,682 560,792 0,792" fill="var(--grey-light)"/>
      <line x1="268" y1="150" x2="284" y2="150" stroke="var(--ink)" stroke-width="1"/>
      <polygon points="284,147 289,150 284,153" fill="var(--ink)"/>
    </svg>
    <header class="block section-head">
      <div class="kicker">Arbeitskraft</div>
      <div class="question">„Haben Sie ohne Arbeitskraft noch ein Einkommen?“</div>
    </header>
    <p class="block small" style="left:40px;top:100px;width:220px">Wer seine Arbeitskraft verliert, verliert auch sein Einkommen. Die gesetzliche Absicherung reicht dabei meist nicht aus, um den eigenen Lebensstandard halten zu können. Gerade zu Beginn des Berufslebens ist der Schutz besonders günstig.</p>
    <p class="block small" style="left:40px;top:200px;width:220px">Jeder vierte Arbeitnehmer wird im Laufe seines Lebens berufsunfähig. Meist sind es nicht Unfälle, sondern Krankheiten, die zum Ausfall führen.</p>
    <div class="block" style="left:40px;top:285px;width:200px;height:70px;display:flex;gap:14px">
      <div class="placeholder" role="img" aria-label="Piktogramm Person 1 von 4" style="width:30px;height:60px"></div>
      <div class="placeholder" role="img" aria-label="Piktogramm Person 2 von 4" style="width:30px;height:60px;margin-top:8px"></div>
      <div class="placeholder" role="img" aria-label="Piktogramm Person 3 von 4, hervorgehoben" style="width:30px;height:60px;margin-top:16px;background:var(--teal)"></div>
      <div class="placeholder" role="img" aria-label="Piktogramm Person 4 von 4" style="width:30px;height:60px;margin-top:24px"></div>
    </div>
    <p class="block small teal-text" style="left:40px;top:370px;width:150px">Können Sie wissen, ob Sie einer der Vier sein werden?</p>

    <p class="block small" style="left:296px;top:100px;width:230px">Die gesetzliche Erwerbsminderungsrente ist gering und wird nur unter strengen Voraussetzungen gezahlt. Eine private Absicherung schließt diese Lücke zuverlässig.</p>
    <p class="block" style="left:296px;top:188px;width:230px;font-weight:700;font-size:10px">Welche Ursachen führen am häufigsten zur Berufsunfähigkeit?</p>
    <div class="block" style="left:290px;top:235px;width:240px;height:190px">
      <div class="stat" style="left:0;top:0"><div class="icon icon--teal" role="img" aria-label="Symbol Bewegungsapparat"></div><div class="num">21 %</div><div class="lbl">Erkrankungen des Bewegungsapparats</div></div>
      <div class="stat" style="left:82px;top:0"><div class="icon" role="img" aria-label="Symbol Herz und Kreislauf"></div><div class="num">7 %</div><div class="lbl">Herz- und Kreislauferkrankungen</div></div>
      <div class="stat" style="left:164px;top:0"><div class="icon" role="img" aria-label="Symbol sonstige Ursachen"></div><div class="num">15 %</div><div class="lbl">Sonstige Erkrankungen</div></div>
      <div class="stat" style="left:0;top:100px"><div class="icon" role="img" aria-label="Symbol Psyche"></div><div class="num">33 %</div><div class="lbl">Psychische Erkrankungen</div></div>
      <div class="stat" style="left:82px;top:100px"><div class="icon" role="img" aria-label="Symbol Unfall"></div><div class="num">9 %</div><div class="lbl">Unfälle</div></div>
      <div class="stat" style="left:164px;top:100px"><div class="icon icon--teal" role="img" aria-label="Symbol Krebs"></div><div class="num">16 %</div><div class="lbl">Krebs und Tumore</div></div>
    </div>

    <div class="block rotated band-statement" style="left:150px;top:489px">Ihr größtes Vermögen ist Ihre Arbeitskraft.</div>
    <div class="block rotated solutions-title" style="left:22px;top:488px">Lösungen der Absicherung Ihrer Arbeitskraft</div>
    <div class="solution" style="left:30px;top:537px">
      <svg viewBox="0 0 24 24" fill="none" stroke="#fff" stroke-width="1.6"><path d="M3 12a9 9 0 0 1 18 0z"/><path d="M12 12v7a2 2 0 0 1-4 0"/></svg>Berufsunfähigkeit
    </div>
    <div class="solution" style="left:150px;top:582px">
      <svg viewBox="0 0 24 24" fill="none" stroke="#fff" stroke-width="1.6"><circle cx="12" cy="12" r="8"/><path d="M8 12h8M12 8v8"/></svg>Grundfähigkeit
    </div>
    <div class="solution" style="left:270px;top:627px">
      <svg viewBox="0 0 24 24" fill="none" stroke="#fff" stroke-width="1.6"><path d="M2 13h5l2-5 4 10 2-5h7"/></svg>Schwere Krankheiten
    </div>
    <div class="block rotated small" style="left:16px;top:628px">Wir haben uns auf die Absicherung der Arbeitskraft spezialisiert.<br>Lassen Sie sich von uns ein individuelles Vorsorgekonzept erstellen.</div>
  </div>

  <div class="page page--longevity">
    <svg class="page-bg" viewBox="0 0 560 792" aria-hidden="true">
      <rect width="560" height="792" fill="var(--paper)"/>
      <polygon points="330,372 560,300 560,520" fill="var(--teal)"/>
      <polygon points="0,650 470,792 410,792 0,682" fill="var(--teal)"/>
      <polygon points="0,682 410,792 0,792" fill="var(--grey-light)"/>
      <line x1="300" y1="548" x2="318" y2="548" stroke="var(--ink)" stroke-width="1"/>
      <polygon points="318,545 323,548 318,551" fill="var(--ink)"/>
    </svg>
    <header class="block section-head">
      <div class="kicker">Langlebigkeit</div>
      <div class="question">„Können Sie Ihr tägliches Leben noch selbst bewältigen?“</div>
    </header>
    <p class="block small" style="left:40px;top:100px;width:300px">Durch die steigende Lebenserwartung wird die Rentenphase immer länger. Gleichzeitig sinkt das Rentenniveau stetig. Wer im Alter seinen Lebensstandard halten will, muss frühzeitig selbst vorsorgen.</p>
    <h2 class="block display" style="left:40px;top:170px;width:360px">Reicht Ihnen<br>Ihre gesetzliche Rente?</h2>
    <table class="block pension-table" style="left:40px;top:255px">
      <tr><td class="head" colspan="2">Renteninformation</td></tr>
      <tr><td>Rentenhöhe lt. Renteninformation</td><td class="amount">1.700 € Brutto</td></tr>
      <tr><td>11 % Beitrag Kranken- &amp; Pflegeversicherung</td><td></td></tr>
      <tr><td>13 % Abzüge Einkommensteuer</td><td></td></tr>
      <tr><td class="head">Netto-Rente</td><td class="amount">1.275 € Netto</td></tr>
      <tr><td>Inflation von 1,5 % jährlich</td><td></td></tr>
      <tr><td>83 % Kaufkraft nach 10 Jahren: 1.110 €</td><td></td></tr>
      <tr><td>73 % Kaufkraft nach 20 Jahren: 935 €</td><td></td></tr>
    </table>
    <div class="block gap-label" style="left:420px;top:372px;width:130px">→ Lücke von<br>800 €/mtl.</div>
    <h2 class="block display" style="left:40px;top:470px;width:500px;font-size:24px">Hier ist Eigenverantwortung gefragt!</h2>
    <p class="block small" style="left:40px;top:515px;width:240px">Die Zahlung einer lebenslangen Rente ist die einzige Möglichkeit, das Langlebigkeitsrisiko abzusichern.</p>
    <p class="block small" style="left:330px;top:530px;width:200px">Andere Produkte können das nicht. Investmentfonds oder Sparguthaben sind irgendwann aufgebraucht.</p>
    <p class="block small" style="left:40px;top:600px;width:460px">Wir arbeiten zusammen mit Ihnen ein individuelles Vorsorgekonzept aus, um die richtigen Weichen so früh wie möglich zu stellen.</p>
  </div>
</section>

<!-- Inside: care and promise -->
<section class="spread spread--care">
  <div class="page page--care">
    <svg class="page-bg" viewBox="0 0 560 792" aria-hidden="true">
      <rect width="560" height="792" fill="var(--paper)"/>
      <polygon points="310,470 560,440 560,720" fill="var(--teal)"/>
      <polygon points="420,792 560,690 560,718 455,792" fill="var(--teal)"/>
      <polygon points="455,792 560,718 560,792" fill="var(--grey-light)"/>
    </svg>
    <header class="block section-head">
      <div class="kicker">Pflege</div>
      <div class="question">„Können Sie sich alt werden auch finanziell leisten?“</div>
    </header>
    <p class="block small" style="left:40px;top:100px;width:460px">Die gesetzliche Pflegeversicherung ist nur eine Teilkaskoversicherung. Sie übernimmt lediglich einen Teil der tatsächlichen Kosten – den Rest tragen Sie oder Ihre Angehörigen.</p>
    <div class="calc-box" style="left:40px;top:160px">
      <span class="calc-icon" role="img" aria-label="Rechner-Symbol"></span>
      <table>
        <tr><td class="title" colspan="2">Pflegegrad 3 – stationär</td></tr>
        <tr><td>Heimkosten mtl.</td><td>3.500 €</td></tr>
        <tr><td>Leistung Pflegekasse</td><td>1.262 €</td></tr>
        <tr><td>Eigenanteil mtl.</td><td class="due">2.238 €</td></tr>
      </table>
    </div>
    <div class="calc-box" style="left:285px;top:205px">
      <span class="calc-icon" role="img" aria-label="Rechner-Symbol"></span>
      <table>
        <tr><td class="title" colspan="2">Pflegegrad 4 – stationär</td></tr>
        <tr><td>Heimkosten mtl.</td><td>4.000 €</td></tr>
        <tr><td>Leistung Pflegekasse</td><td>1.775 €</td></tr>
        <tr><td>Eigenanteil mtl.</td><td class="due">2.225 €</td></tr>
      </table>
    </div>
    <p class="block center-q" style="left:100px;top:320px">Können Sie sich das leisten?</p>
    <p class="block small" style="left:40px;top:345px;width:220px">Die Kosten für Pflege steigen stetig und werden oft unterschätzt.</p>
    <p class="block small" style="left:285px;top:345px;width:225px">Wer nicht vorsorgt, greift auf Erspartes zurück oder belastet seine Familie.</p>
    <h2 class="block display" style="left:40px;top:395px;width:330px">Pflegebedürftigkeit…<br>es kann jeden treffen!</h2>
    <p class="block small" style="left:40px;top:470px;width:260px">Pflegebedürftig wird man nicht nur im Alter. Auch Unfälle oder Krankheiten können in jungen Jahren zu einem dauerhaften Pflegefall führen – mit hohen Kosten über viele Jahre.</p>
    <p class="block tiny white" style="left:420px;top:485px;width:130px;text-align:right"><strong style="font-size:10px">2,5 Millionen Menschen</strong><br>sind in Deutschland pflegebedürftig – Tendenz steigend.</p>
    <h2 class="block display" style="left:40px;top:590px;width:330px">Eines bleibt aber gleich:</h2>
    <p class="block small" style="left:40px;top:630px;width:290px">Die gesetzliche Pflegeabsicherung allein reicht nicht aus.</p>
    <p class="block small" style="left:40px;top:680px;width:320px">Wir helfen Ihnen dabei, diese Lücke zu schließen, indem wir mit Ihnen einen passenden Vorsorgeplan ausarbeiten.</p>
  </div>

  <div class="page page--promise">
    <svg class="page-bg" viewBox="0 0 560 792" aria-hidden="true">
      <defs>
        <linearGradient id="photoTone" x1="0" y1="0" x2="1" y2="1">
          <stop offset="0" stop-color="#6d5a34"/>
          <stop offset=".5" stop-color="#b79a4c"/>
          <stop offset="1" stop-color="#e6d27a"/>
        </linearGradient>
      </defs>
      <rect width="560" height="792" fill="var(--paper)"/>
      <polygon points="0,0 560,0 560,160 0,232" fill="url(#photoTone)" role="img" aria-label="Foto: Laufschuhe eines Joggers auf einer sonnigen Strecke"/>
      <polygon points="0,232 560,160 560,176 0,252" fill="var(--teal)"/>
    </svg>
    <h2 class="block display" style="left:40px;top:290px;width:480px">Wir stehen für:<br>TOP Bedingungen<br>den besten Versicherungsschutz</h2>
    <p class="block small" style="left:40px;top:420px;width:460px">Die meisten Menschen sind sich der beschriebenen Probleme der fehlenden Absicherung der Arbeitskraft, der Altersrente und des Pflegerisikos sehr wohl bewusst. Allerdings mangelt es noch an Handlungen.</p>
    <p class="block small" style="left:40px;top:478px;width:460px">Dies liegt sehr oft daran, dass der Ansprechpartner fehlt.</p>
    <p class="block small" style="left:40px;top:505px;width:460px">Genau hier wollen wir uns auf Ihre Seite stellen und es zu unserer Aufgabe machen, Sie mit den besten Bedingungen zu überzeugen und zu gewinnen.</p>
  </div>
</section>

</body>
</html>
```